Saffron Lantern Court Business Card

I am looking for a business card desgined for my restaurant. It is an Indian restaurant, we are looking for something thats modern, yet traditional with the indian culture, we are looking for colors that match our logo. The logo is a design of the building with the name of the restaurant. for more information on the restaurant go to www.saffronlanterncourt.example

Industry/Entity Type

Indian Restaurant

Contact Information for Business Card

we are looking for somthing thats modern, yet traditional with the indian culture, we are looking for colors that match our logo. The logo is a design of the building with the name of the restaurant. for more information on the restaurant go to www.saffronlanterncourt.example

Requirements
Must have
• The logo that is attached,
• Name: Harvinder Oberoi,
• address of the restaurant: 7328 West Larkspur Rd, Phoenix, Arizona, 85213
• Phone: (602) 555-0147
• Fax: (602) 555-0193
• Restaurant Catering Banquet
• Website: www.SaffronLanternCourt.example
Nice to have
• wanted to get something that goes with the theme of the restaurant, which is traditional but also keep a very professional and modern touch

```html
<!DOCTYPE html>
<html lang="en">
<head>
<meta charset="utf-8">
<title>Saffron Lantern Court — Business Card</title>
<link rel="stylesheet" href="https://fonts.googleapis.com/css2?family=Open+Sans:wght@400;600;700&display=swap">
<style>
  :root {
    --brand-red: #a52228;
    --card-white: #ffffff;
    --ink: #1c1c1c;
    --backdrop: #e8e5e1;
  }
  * { margin: 0; padding: 0; box-sizing: border-box; }
  html, body {
    width: 1200px; height: 1000px; overflow: hidden;
    background: var(--backdrop);
    font-family: "Open Sans", Arial, sans-serif;
  }
  .canvas { position: relative; width: 1200px; height: 1000px; }
  .card {
    position: absolute; left: 266px; width: 666px; height: 396px;
    box-shadow: 0 3px 10px rgba(0,0,0,0.18);
  }
  .card--front { top: 74px; background: var(--card-white); }
  .card--back { top: 534px; background: var(--brand-red); }
  .card__frame {
    position: absolute; left: 19px; top: 17px; right: 18px; bottom: 14px;
    border: 2px solid var(--brand-red);
  }
  .wordmark {
    position: absolute; text-align: center; font-weight: 700;
    line-height: 1.05; letter-spacing: 1px; text-transform: uppercase;
  }
  .card--front .wordmark {
    left: 62px; width: 240px; top: 138px; font-size: 44px; color: var(--brand-red);
  }
  .card--back .wordmark {
    left: 183px; width: 300px; top: 123px; font-size: 50px; color: var(--card-white);
  }
  .contact { position: absolute; left: 344px; top: 100px; color: var(--ink); }
  .contact__name {
    font-size: 19px; font-weight: 700; color: var(--brand-red);
    letter-spacing: 0.3px; margin-bottom: 16px;
  }
  .contact__services { font-size: 15.5px; margin-bottom: 6px; }
  .contact__address { font-size: 15.5px; line-height: 21px; margin-bottom: 12px; }
  .contact__line { display: flex; align-items: center; font-size: 15.5px; line-height: 23px; }
  .contact__line svg { width: 12px; height: 12px; margin-right: 5px; fill: var(--brand-red); }
</style>
</head>
<body>
<main class="canvas">
  <section class="card card--front" aria-label="Business card front">
    <div class="card__frame"></div>
    <div class="wordmark">Saffron<br>Lantern<br>Court</div>
    <div class="contact">
      <p class="contact__name">HARVINDER OBEROI</p>
      <p class="contact__services">Restaurant Catering Banquet</p>
      <p class="contact__address">7328 West Larkspur Rd,<br>Phoenix, Arizona, 85213</p>
      <p class="contact__line">
        <svg viewBox="0 0 12 12" aria-hidden="true"><path d="M1 4c0-2 2-3 5-3s5 1 5 3l-2 1-1-1.5H4L3 5zM2.5 6h7l1 5h-9z"/></svg>
        (602) 555-0147
      </p>
      <p class="contact__line">
        <svg viewBox="0 0 12 12" aria-hidden="true"><path d="M3 1h6v3H3zM1 5h10v4H9v2H3V9H1zM4 8v2h4V8z"/></svg>
        (602) 555-0193
      </p>
      <p class="contact__line">
        <svg viewBox="0 0 12 12" aria-hidden="true"><circle cx="5" cy="5" r="4.2" fill="none" stroke="#a52228" stroke-width="1.4"/><path d="M6 6l5 2-2 1-1 2z"/></svg>
        www.SaffronLanternCourt.example
      </p>
    </div>
  </section>

  <section class="card card--back" aria-label="Business card back">
    <div class="wordmark">Saffron<br>Lantern<br>Court</div>
  </section>
</main>
</body>
</html>
```